KTW Structural Approval Partners Certifiers

Professional Construction Consultancy Company Business Card - must keep logo colours see images below - examples have been added from my last competition - please see them as examples only!

Target Market(s)

Home Builders

Industry/Entity Type

Construction

Contact Information for Business Card

See "must haves"

Font styles to use
Sans Serif

Colors
ffffff
add136
000000

Requirements
Must have
• Daniel Moravec
• Director
• Phone: 0431 758 219
• Address: 17 Corrigan St,
• Holloway Vale, SA, 5098
• Email: ktwapprovalpartners@mailbox-example.com
• Website: www.ktwapprovalpartners.example.au
• Facebook: KTW Structural Approval Partners
Nice to have
• Side 1: full logo
• Side 2: company details
Should not have
• hard to read
• must be clear and professional

```html
<!DOCTYPE html>
<html lang="en">
<head>
<meta charset="utf-8">
<title>KTW Structural Approval Partners – Business Card</title>
<link rel="stylesheet" href="https://fonts.googleapis.com/css2?family=Montserrat:wght@400;500;600;700&family=Roboto+Condensed:wght@700&display=swap">
<style>
  :root {
    --paper: #ffffff;
    --lime: #add136;
    --ink: #000000;
    --charcoal: #1c1c1c;
    --backdrop: #2b2b2b;
    --text: #1a1a1a;
  }
  * { box-sizing: border-box; margin: 0; padding: 0; }
  html, body { width: 1200px; height: 900px; overflow: hidden; }
  body {
    background: var(--backdrop);
    font-family: "Montserrat", Arial, sans-serif;
    color: var(--text);
    position: relative;
  }
  .card {
    position: absolute;
    left: 325px;
    width: 558px;
    height: 305px;
    background: var(--paper);
    overflow: hidden;
  }
  .card--front { top: 129px; }
  .card--back { top: 477px; }

  .card__band {
    position: absolute;
    left: 0; right: 0; bottom: 0;
    height: 22px;
    display: flex;
  }
  .card__band span { flex: 1; }
  .band-dark { background: var(--charcoal); }
  .band-lime { background: var(--lime); }

  /* Front */
  .front-mark {
    position: absolute;
    top: 108px; left: 0; right: 0;
    display: flex;
    justify-content: center;
    align-items: center;
    gap: 14px;
  }
  .front-mark__square {
    width: 62px; height: 62px;
    background: var(--lime);
  }
  .front-mark__name {
    font-weight: 600;
    font-size: 20px;
    line-height: 1.2;
    color: var(--ink);
    letter-spacing: 0.5px;
  }
  .social {
    position: absolute;
    top: 241px; left: 0; right: 0;
    display: flex;
    justify-content: center;
    align-items: center;
    gap: 8px;
    font-size: 14px;
  }
  .social__square {
    width: 15px; height: 15px;
    background: var(--lime);
    border-radius: 2px;
  }

  /* Back */
  .back-mark {
    position: absolute;
    top: 24px; left: 24px;
    display: flex;
    align-items: center;
    gap: 10px;
  }
  .back-mark__square {
    width: 44px; height: 44px;
    background: var(--lime);
  }
  .back-mark__name {
    font-weight: 600;
    font-size: 14px;
    line-height: 1.25;
    color: var(--ink);
  }
  .company {
    position: absolute;
    top: 142px; left: 24px;
    font-size: 14px;
    line-height: 18px;
  }
  .company__title { color: var(--lime); }
  .company__title b { font-weight: 700; }
  .contacts {
    position: absolute;
    top: 218px; left: 24px;
    list-style: none;
    font-size: 14px;
    line-height: 18.5px;
  }
  .contacts li { display: flex; align-items: center; gap: 8px; white-space: nowrap; }
  .contacts svg { width: 13px; height: 13px; flex: none; }
  .person {
    position: absolute;
    top: 226px; right: 22px;
    white-space: nowrap;
  }
  .person__name {
    font-family: "Roboto Condensed", Arial, sans-serif;
    font-weight: 700;
    font-size: 22px;
    color: var(--lime);
    text-transform: uppercase;
    line-height: 1;
  }
  .person__role { font-size: 14px; line-height: 17px; margin-top: 5px; }
</style>
</head>
<body>

<section class="card card--front" aria-label="Business card front">
  <div class="front-mark">
    <div class="front-mark__square"></div>
    <div class="front-mark__name">KTW Structural Approval Partners<br>Certifiers</div>
  </div>
  <div class="social">
    <span class="social__square"></span>
    <span>KTW Structural Approval Partners</span>
  </div>
  <div class="card__band"><span class="band-dark"></span><span class="band-lime"></span></div>
</section>

<section class="card card--back" aria-label="Business card back">
  <div class="back-mark">
    <div class="back-mark__square"></div>
    <div class="back-mark__name">KTW Structural Approval Partners<br>Certifiers</div>
  </div>

  <div class="company">
    <div class="company__title"><b>KTW</b> Structural Approval Partners</div>
    <div>17 Corrigan St, Holloway Vale</div>
    <div>SA, 5098</div>
  </div>

  <ul class="contacts">
    <li>
      <svg viewBox="0 0 16 16" aria-hidden="true"><path fill="#add136" d="M3.6 1.5l2.3 2.6-1.2 1.8c.9 2 2.5 3.6 4.4 4.5l1.8-1.2 2.6 2.3-1.2 2.3C7.4 14.6 1.4 8.6 1.3 3z"/></svg>
      <span>0431 758 219</span>
    </li>
    <li>
      <svg viewBox="0 0 16 16" aria-hidden="true"><rect x="1" y="3" width="14" height="10" rx="1" fill="#add136"/><path d="M1.5 3.5L8 9l6.5-5.5" stroke="#fff" stroke-width="1.3" fill="none"/></svg>
      <span>ktwapprovalpartners@mailbox-example.com</span>
    </li>
    <li>
      <svg viewBox="0 0 16 16" aria-hidden="true"><circle cx="8" cy="8" r="6.5" fill="none" stroke="#add136" stroke-width="1.6"/><path d="M1.5 8h13M8 1.5c-3 3.5-3 9.5 0 13M8 1.5c3 3.5 3 9.5 0 13" stroke="#add136" stroke-width="1.2" fill="none"/></svg>
      <span>www.ktwapprovalpartners.example.au</span>
    </li>
  </ul>

  <div class="person">
    <div class="person__name">Daniel Moravec</div>
    <div class="person__role">Director</div>
  </div>

  <div class="card__band"><span class="band-lime"></span><span class="band-dark"></span></div>
</section>

</body>
</html>
```